"Vows and Farewells by Meg" Web Site

I would like a web site designed for my funeral and wedding celebrancy business. My logo was designed by Artboard Hive (attached). I have written content of the web pages for reference (attached). I have attached logos designed through artboard hive and photos.
I am sure what else to write in a project description and would welcome suggestions

Target Market(s)

for marriages - brides and grooms, for funerals - families who have lost a loved one

Industry/Entity Type

Wedding Planner

Number of Pages Required

4 page

Font styles to use
Sans Serif

Colors
886aae
3277b5
33a6d7
a64599
e34096

Requirements
Must have
• a call to action (contact me) throughout
Nice to have
• nil
Should not have
• no morbid images

```html
<!DOCTYPE html>
<html lang="en">
<head>
<meta charset="utf-8">
<title>Vows and Farewells by Meg</title>
<link href="https://fonts.googleapis.com/css2?family=Roboto+Slab:wght@300;400&family=Roboto:wght@400;500;700&family=Open+Sans:wght@400;600&family=Montserrat:wght@600&display=swap" rel="stylesheet">
<style>
  :root {
    --lavender: #886aae;
    --nav-purple: #7f6cb3;
    --deep-blue: #3277b5;
    --sky-blue: #33a6d7;
    --plum: #a64599;
    --magenta: #e34096;
    --button: #d6287f;
    --footer: #704f9e;
    --ink: #444;
    --white: #fff;
  }
  * { margin: 0; padding: 0; box-sizing: border-box; }
  html, body { width: 1200px; height: 2258px; overflow: hidden; background: var(--white); }
  .page { position: relative; width: 1200px; height: 2258px; overflow: hidden; font-family: "Open Sans", sans-serif; color: var(--ink); }

  /* Header */
  .site-header { position: absolute; top: 0; left: 0; width: 1200px; height: 110px; background: var(--white); }
  .brand { position: absolute; left: 115px; top: 25px; display: flex; align-items: center; gap: 12px; }
  .brand-dot { width: 58px; height: 58px; border-radius: 50%; background: var(--lavender); }
  .brand-name { font-family: "Roboto Slab", serif; font-weight: 400; font-size: 21px; color: var(--nav-purple); white-space: nowrap; }
  .main-nav { position: absolute; top: 45px; left: 487px; display: flex; gap: 28px; font-family: "Roboto", sans-serif; font-size: 16px; }
  .main-nav a { color: var(--nav-purple); text-decoration: none; }
  .main-nav a.is-current { color: #3d2f7a; font-weight: 500; }

  /* Hero */
  .hero { position: absolute; top: 110px; left: 0; width: 1200px; height: 565px; }
  .hero-photo { position: absolute; inset: 0; background: linear-gradient(180deg, #6f8796 0%, #5d7a88 38%, #4d6b78 55%, #8c8478 72%, #b7a893 100%); }
  .hero-title { position: absolute; top: 195px; width: 100%; text-align: center; color: var(--white); font-family: "Roboto Slab", serif; font-weight: 300; }
  .hero-title .kicker { display: block; font-size: 50px; letter-spacing: 1px; line-height: 60px; }
  .hero-title .headline { display: block; font-size: 56px; font-weight: 400; letter-spacing: 1px; line-height: 68px; }
  .slider-dots { position: absolute; top: 527px; left: 553px; display: flex; gap: 8px; }
  .slider-dots span { width: 15px; height: 15px; border-radius: 50%; background: var(--white); }
  .slider-dots span.is-active { background: transparent; border: 2px solid var(--white); }

  /* About */
  .about { position: absolute; top: 675px; left: 0; width: 1200px; height: 440px; text-align: center; }
  .section-title { font-family: "Roboto Slab", serif; font-weight: 400; font-size: 37px; }
  .about .section-title { position: absolute; top: 64px; width: 100%; color: #2f93cf; }
  .about-copy { position: absolute; top: 126px; left: 190px; width: 820px; font-size: 13px; line-height: 17px; color: #4a4a4a; }
  .about-copy p { margin-bottom: 9px; }
  .btn-contact { position: absolute; top: 337px; left: 516px; width: 170px; height: 39px; background: var(--button); color: var(--white); font-family: "Montserrat", sans-serif; font-weight: 600; font-size: 15px; line-height: 39px; letter-spacing: 0.5px; text-decoration: none; }

  /* Services */
  .services { position: absolute; top: 1020px; left: 0; width: 1200px; height: 608px; }
  .services-bg { position: absolute; inset: 0; }
  .services .section-title { position: absolute; top: 147px; width: 100%; text-align: center; color: var(--white); }
  .service { position: absolute; top: 215px; width: 300px; text-align: center; color: var(--white); }
  .service-ring { width: 240px; height: 240px; margin: 0 auto; border: 2px solid var(--white); border-radius: 50%; padding: 8px; }
  .service-photo { width: 100%; height: 100%; border-radius: 50%; }
  .service h3 { margin-top: 15px; font-family: "Roboto", sans-serif; font-weight: 500; font-size: 20px; }
  .service p { margin-top: 6px; font-size: 12px; line-height: 19px; }
  .service--marriages { left: 143px; }
  .service--funerals { left: 449px; }
  .service--other { left: 750px; }

  /* Contact */
  .contact { position: absolute; top: 1628px; left: 0; width: 1200px; height: 465px; }
  .contact-photo { position: absolute; inset: 0; background: linear-gradient(120deg, #d9d4cf 0%, #c9bfb4 35%, #a0896f 65%, #6f5a48 100%); }
  .contact-panel { position: absolute; inset: 0; }
  .contact-details { position: absolute; top: 110px; left: 600px; width: 480px; text-align: center; }
  .contact-details .section-title { color: #2e6db3; font-size: 38px; }
  .contact-name { margin-top: 20px; font-family: "Roboto", sans-serif; font-size: 20px; color: #c5338c; }
  .contact-line { margin-top: 22px; font-size: 17px; color: #222; display: flex; justify-content: center; align-items: center; gap: 6px; }
  .contact-line svg { fill: var(--magenta); }

  /* Footer */
  .site-footer { position: absolute; top: 2093px; left: 0; width: 1200px; height: 165px; background: var(--footer); color: var(--white); }
  .footer-nav { position: absolute; top: 35px; left: 131px; display: flex; gap: 20px; font-family: "Roboto", sans-serif; font-size: 15px; }
  .footer-nav a { color: var(--white); text-decoration: none; }
  .copyright { position: absolute; top: 70px; left: 131px; font-size: 12px; }
  .social { position: absolute; top: 34px; left: 903px; display: flex; gap: 6px; }
  .social span { width: 38px; height: 38px; border: 2px solid var(--white); border-radius: 50%; }
</style>
</head>
<body>
<div class="page">

  <header class="site-header">
    <div class="brand">
      <span class="brand-dot"></span>
      <span class="brand-name">Vows and Farewells by Meg</span>
    </div>
    <nav class="main-nav">
      <a class="is-current" href="#">Home</a>
      <a href="#">About Me</a>
      <a href="#">Marriages</a>
      <a href="#">Funerals</a>
      <a href="#">Other Ceremonies</a>
      <a href="#">Contact Me</a>
    </nav>
  </header>

  <section class="hero">
    <div class="hero-photo" role="img" aria-label="Celebrant greeting guests at a beach wedding by the sea"></div>
    <h1 class="hero-title">
      <span class="kicker">WELCOME TO</span>
      <span class="headline">VOWS AND FAREWELLS BY MEG</span>
    </h1>
    <div class="slider-dots"><span class="is-active"></span><span></span><span></span><span></span></div>
  </section>

  <section class="about">
    <h2 class="section-title">About Us</h2>
    <div class="about-copy">
      <p>Thank you for visiting ‘Vows and Farewells by Meg’. Whether you are planning a wedding with the love of your life, a funeral to celebrate the life of a loved one or one of many other love and life celebrations, I am glad that you came to ‘Vows and Farewells by Meg’.</p>
      <p>My name is Meg Harrow and I am the owner of this business. My mission is to work with you to create a marriage, funeral or celebration service that truly celebrates love and life in an authentic way. Your way!</p>
      <p>I am legally authorised by the Commonwealth Attorney General’s department to perform marriages across Australia and have completed a certificate IV in Celebrancy which included Marriage celebrancy units and Funeral celebrancy units My commitment to you is that I will spend time with you, get to know you, listen to your dreams and desires for your celebration. We can then create a service that is unique, special and memorable.</p>
      <p>Please contact me to discuss your needs</p>
    </div>
    <a class="btn-contact" href="#">CONTACT</a>
  </section>

  <section class="services">
    <svg class="services-bg" width="1200" height="608" viewBox="0 0 1200 608" aria-hidden="true">
      <defs>
        <linearGradient id="servicesGradient" x1="0" y1="0" x2="1" y2="1">
          <stop offset="0" stop-color="#2f95d0"/>
          <stop offset="0.5" stop-color="#3a55a0"/>
          <stop offset="0.78" stop-color="#8a3f97"/>
          <stop offset="1" stop-color="#e0288a"/>
        </linearGradient>
      </defs>
      <path d="M0 0 Q600 170 1200 0 L1200 608 L0 608 Z" fill="url(#servicesGradient)"/>
    </svg>
    <h2 class="section-title">Our Services</h2>
    <div class="service service--marriages">
      <div class="service-ring"><div class="service-photo" role="img" aria-label="Celebrant standing with a bride in a garden" style="background:linear-gradient(160deg,#7a9a5a,#c9c0b4 60%,#3a3a3a)"></div></div>
      <h3>Marriages</h3>
      <p>Class aptent taciti sociosqu ad litora<br>torquent per conubia nostra</p>
    </div>
    <div class="service service--funerals">
      <div class="service-ring"><div class="service-photo" role="img" aria-label="Celebrant speaking at a microphone during a service" style="background:linear-gradient(160deg,#e8e6e2,#c9b39a 60%,#e7b0a0)"></div></div>
      <h3>Funerals</h3>
      <p>Class aptent taciti sociosqu ad litora<br>torquent per conubia nostra</p>
    </div>
    <div class="service service--other">
      <div class="service-ring"><div class="service-photo" role="img" aria-label="Celebrant speaking at a lectern for a ceremony" style="background:linear-gradient(160deg,#e9dcd6,#b89a85 55%,#d9503f)"></div></div>
      <h3>Other Ceremonies</h3>
      <p>Class aptent taciti sociosqu ad litora<br>torquent per conubia nostra</p>
    </div>
  </section>

  <section class="contact">
    <div class="contact-photo" role="img" aria-label="Celebrant speaking into a microphone at an indoor celebration"></div>
    <svg class="contact-panel" width="1200" height="465" viewBox="0 0 1200 465" aria-hidden="true">
      <path d="M640 0 Q520 232 648 465 L1200 465 L1200 0 Z" fill="#fff"/>
    </svg>
    <div class="contact-details">
      <h2 class="section-title">Contact Me</h2>
      <div class="contact-name">Meg Harrow</div>
      <div class="contact-line">
        <svg width="11" height="15" viewBox="0 0 12 16"><path d="M6 0C2.7 0 0 2.6 0 5.9 0 10.3 6 16 6 16s6-5.7 6-10.1C12 2.6 9.3 0 6 0zm0 8.2a2.3 2.3 0 1 1 0-4.6 2.3 2.3 0 0 1 0 4.6z"/></svg>
        <span>P.O Box 218, Riverton 6148, Western Australia</span>
      </div>
      <div class="contact-line">
        <svg width="15" height="15" viewBox="0 0 16 16"><path d="M3.5 0.5l2.6 3.2-1.6 2.1c0.9 2 2.5 3.6 4.5 4.5l2.1-1.6 3.2 2.6-1.3 3c-6.6-0.3-11.9-5.6-12.2-12.2z"/></svg>
        <span>Phone: (+61) 0400 555 123</span>
      </div>
      <div class="contact-line">
        <svg width="16" height="13" viewBox="0 0 16 12"><path d="M0 0h16v1.5L8 6.8 0 1.5z"/><path d="M0 3.2l8 5.3 8-5.3V12H0z"/></svg>
        <span>Email: meg@vowsfarewells.example</span>
      </div>
    </div>
  </section>

  <footer class="site-footer">
    <nav class="footer-nav">
      <a href="#">Home</a>
      <a href="#">About Me</a>
      <a href="#">Marriages</a>
      <a href="#">Funerals</a>
      <a href="#">Other Ceremonies</a>
      <a href="#">Contact Me</a>
    </nav>
    <p class="copyright">© 2018 Company Name&nbsp; All right reserved</p>
    <div class="social" aria-label="Social links"><span></span><span></span><span></span><span></span></div>
  </footer>

</div>
</body>
</html>
```